Torvaline business cards

Need fresh design for our business cards. Logo must be specific, we are open for everything else.

Contact Information for Business Card

phrase "GMP & JANITORIAL SERVICES" should be used as main point of card

Colors
3176b5
3276b5
85acd3
cedeed
ffffff
0292cd
33a6d7
85cae6
cee9f5

Requirements
Must have
• The logo
Should not have
• crowded designs

```html
<!DOCTYPE html>
<html lang="en">
<head>
<meta charset="utf-8">
<title>Torvaline business cards</title>
<link rel="stylesheet" href="https://fonts.googleapis.com/css2?family=Lato:wght@400;700&display=swap">
<style>
  :root {
    --stage: #262729;
    --brand-blue: #1a80c2;
    --brand-blue-soft: #4b9bd0;
    --ink: #2a2a2a;
    --rule: #7d7d7d;
    --paper: #ffffff;
  }
  * { box-sizing: border-box; margin: 0; padding: 0; }
  html, body {
    width: 1200px; height: 895px; overflow: hidden;
    background: var(--stage);
    font-family: "Lato", Arial, sans-serif;
  }
  .stage {
    width: 1200px; height: 895px;
    display: flex; flex-direction: column;
    align-items: center; justify-content: center; gap: 40px;
  }
  .card {
    width: 640px; height: 366px; position: relative; overflow: hidden;
    box-shadow: 0 10px 30px rgba(0,0,0,.45);
  }
  .card-back {
    background: var(--brand-blue);
    display: flex; align-items: center; justify-content: center;
  }
  .wordmark {
    display: flex; align-items: center; gap: 14px;
    font-weight: 400; letter-spacing: 0.14em; line-height: 1;
  }
  .wordmark-dot {
    width: 14px; height: 14px; border-radius: 50%;
  }
  .card-back .wordmark { font-size: 58px; color: var(--brand-blue-soft); }
  .card-back .wordmark-dot { background: var(--brand-blue-soft); }

  .card-front { background: var(--paper); }
  .card-front .wordmark {
    position: absolute; top: 62px; left: 150px;
    font-size: 50px; color: var(--brand-blue);
  }
  .card-front .wordmark-dot { background: var(--brand-blue); }

  .contact-list {
    position: absolute; top: 168px; right: 318px;
    list-style: none; text-align: right;
    font-size: 17px; color: var(--ink); line-height: 27px;
  }
  .contact-list li { display: flex; justify-content: flex-end; align-items: center; gap: 14px; }
  .contact-list svg { width: 14px; height: 14px; fill: var(--brand-blue); }
  .divider {
    position: absolute; top: 162px; left: 340px;
    width: 1px; height: 88px; background: var(--rule);
  }
  .person {
    position: absolute; top: 166px; left: 360px;
  }
  .person-name { font-size: 28px; color: var(--brand-blue); font-weight: 400; }
  .person-role { font-size: 16px; color: var(--ink); margin-top: 2px; }

  .service-band {
    position: absolute; left: 0; right: 0; top: 282px; height: 34px;
    background: var(--brand-blue); color: var(--paper);
    font-weight: 700; font-size: 17px; letter-spacing: 0.04em;
    display: flex; align-items: center; padding-left: 150px;
  }
</style>
</head>
<body>
<main class="stage">
  <section class="card card-back" aria-label="Card back">
    <div class="wordmark"><span class="wordmark-name">TORVALINE</span><span class="wordmark-dot"></span></div>
  </section>

  <section class="card card-front" aria-label="Card front">
    <div class="wordmark"><span class="wordmark-name">TORVALINE</span><span class="wordmark-dot"></span></div>

    <ul class="contact-list">
      <li>000 000 0000
        <svg viewBox="0 0 24 24" aria-hidden="true"><path d="M6.6 10.8a15.1 15.1 0 0 0 6.6 6.6l2.2-2.2c.3-.3.7-.4 1-.2 1.1.4 2.3.6 3.6.6.6 0 1 .4 1 1V20c0 .6-.4 1-1 1A17 17 0 0 1 3 4c0-.6.4-1 1-1h3.5c.6 0 1 .4 1 1 0 1.3.2 2.5.6 3.6.1.3 0 .7-.2 1z"/></svg>
      </li>
      <li>info@torvaline.com
        <svg viewBox="0 0 24 24" aria-hidden="true"><path d="M2 5h20v14H2z M2 5l10 8 10-8" fill="var(--brand-blue)"/><path d="M3 6l9 7 9-7" fill="none" stroke="#fff" stroke-width="1.6"/></svg>
      </li>
      <li>www.torvaline.com
        <svg viewBox="0 0 24 24" aria-hidden="true"><circle cx="12" cy="12" r="10"/><path d="M2 12h20M12 2c3 3 3 17 0 20M12 2c-3 3-3 17 0 20M4 7h16M4 17h16" fill="none" stroke="#fff" stroke-width="1.3"/></svg>
      </li>
    </ul>

    <div class="divider"></div>

    <div class="person">
      <p class="person-name">Dana Whitlow</p>
      <p class="person-role">Managing Partner</p>
    </div>

    <div class="service-band">GMP &amp; JANITORIAL SERVICES</div>
  </section>
</main>
</body>
</html>
```